Since the attack on the Brookfield Plaza in Nairobi on September 21st, 2013 Nairobi citizens have lived in a state of mourning, fear and shock. We believe that a healthy society, in a nation whose unofficial motto is Peace, Love and Unity needs to remember these words now more than ever. Whilst other attacks, emergencies and national dilemmas seem likely in the next few years, we the Kenyan citizenry, cannot let a four- day siege in our nation’s capital city, pass without a meaningful national conversation.
The “Our Nairobi: A Brookfield Memorial” project aims to address this. It is not an investigation. It is a powerful memorial that draws its inspiration from a similar effort undertaken by Pulse Weekly and the citizens of New York after the September 11 attack: http://content.pulseweekly-demo.com/pulse/afterfall/
Part of the memorial consists of interviews with those personally affected by the attack. They were all asked one question: “What were you doing the morning of the attack?”
Drawing on filmmaker Dev Malhotra’s previous work on creating a news piece with the GNR (http://www.gnr-demo.com/news/in-pictures-58174203), the result is a moving collection of stories that have one overall message: Unity. People of all faiths, backgrounds and age come together in this project with a desire to achieve peace, love and unity for Kenya’s future generations.
http://clipvault-demo.com/filmsavanna/brookfield-multimedia-project
Password: lanternhill
The link above provides an example of the interviews taken. Please take a moment to view at least one video to gain an impression of the project.
A wide cross-section of society has already shown support for this project, from Silver Shield Aid representatives, to police officers, and foreign ambassadors. The aim is to edit 40 pieces and present the films at an exhibition on the 21st of September at the Nairobi Heritage Gallery where victims, dignitaries and the general public will be invited to mark the one-year anniversary of the attack. The website, www.brookfieldmemorial-demo.org will be launched simultaneously with links to the GNR and other media outlets for national and global coverage. The exhibition itself will run for 2 months.
Please be part of this memorial project and help make it come to life. It is no small endeavor to collate these stories, host the memorial event and exhibition and create the website, but with your help it is achievable. We are all part of this story, and we would be honored if you would partner with us to make this story heard.

I need to have the basic website up by the 25th August in order to have sponsors believe that I will do it. The site must go live at the start of next month, with probably 20 videos up .... I then need to add videos....I imagine many of the features that the Pulse site has (videos popping up embedded in the site with the rest of the site as wall paper) - but with a sponsors page which can have the story of the sponsors integrated in the same way that the portraits are integrated - so when you click a logo maybe you get a write up of how the company participated in the project....I also like the function of having the names of the participants back link to the photographs - and having people being able to share on friendnet or chirper the story -

I am having logos designed for Acacia Ridge Prodcutions, and perhaps that can be the name that appears rather than Pulse Weekly

I want the site to be elegant, unlcuttered - maybe using a turcoise or blue as a single color just as pulse used Red.....

I may have support from a company in Kenya as I am not a web designer and will need to continue to upload films - therefore HTML will probably be the best option with a CMS for future editing and updating. Or you can give a maintenance contract - it'll be unlikely that it grows beyond the 40 stories I am intending - so either that or perhaps you could privide the raw files for HTML and PHP for future updating with a chap here....

I'm happy to keep my pro account at ClipVault if that helps as hosting - remember Kenyan internet speeds are considerably slower than outside -

That's all for now. Thank you for considering work on this important project.

Yours truly

Dev Malhotra

www.filmsavanna-demo.com

```html
<!DOCTYPE html>
<html lang="en">
<head>
<meta charset="utf-8">
<title>Our Nairobi: A Brookfield Memorial</title>
<link href="https://fonts.googleapis.com/css2?family=Open+Sans:wght@300;400;600;700&display=swap" rel="stylesheet">
<style>
  :root {
    --accent: #67a3c6;
    --accent-nav: #5d9cc4;
    --ink: #2b2b2b;
    --muted: #8a8a8a;
    --card: #f6f6f6;
    --rule: #c9d3e2;
    --footer: #67a3c5;
    --footer-text: #eef5fa;
    --footer-label: #d3e6f2;
    --white: #ffffff;
  }
  * { box-sizing: border-box; margin: 0; padding: 0; }
  html, body { width: 848px; height: 1200px; overflow: hidden; background: var(--white); }
  body { font-family: "Open Sans", Arial, sans-serif; color: var(--ink); }
  .page { position: relative; width: 848px; height: 1200px; overflow: hidden; }

  .masthead { position: absolute; left: 0; top: 0; width: 848px; height: 515px; background: #fbfbfb; }
  .site-nav { position: absolute; right: 60px; top: 34px; display: flex; gap: 12px; }
  .site-nav a { font-size: 9.5px; font-weight: 700; color: var(--ink); text-decoration: none; letter-spacing: -0.1px; text-transform: uppercase; }
  .site-nav a.is-active { color: var(--accent-nav); }
  .hero { position: absolute; left: 68px; top: 69px; width: 722px; height: 388px;
    background:
      radial-gradient(ellipse 30% 60% at 95% 35%, rgba(40,34,28,0.75), rgba(40,34,28,0) 100%),
      radial-gradient(ellipse 40% 30% at 20% 78%, rgba(150,120,90,0.45), rgba(150,120,90,0) 100%),
      linear-gradient(180deg, #8d9296 0%, #857d74 8%, #7a6f64 18%, #6e6a66 28%, #86766a 40%, #7d6756 55%, #6f5948 72%, #5f4c3d 88%, #4d3e33 100%); }
  .masthead-rule { position: absolute; left: 10px; top: 494px; width: 838px; height: 2px; background: var(--rule); }

  .features { position: absolute; left: 69px; top: 543px; display: flex; gap: 18px; }
  .feature { width: 164px; height: 169px; background: var(--card); position: relative; text-align: center; }
  .feature h3 { font-size: 11px; font-weight: 700; margin-top: 17px; }
  .feature svg { display: block; margin: 9px auto 0; }
  .feature p { font-size: 8px; line-height: 12.5px; color: var(--muted); padding: 0 20px; margin-top: 9px; }
  .feature .btn { position: absolute; left: 0; bottom: 0; width: 100%; height: 35px; line-height: 35px;
    background: var(--accent); color: var(--white); font-size: 8.5px; font-weight: 700; }
  .section-rule { position: absolute; left: 69px; top: 745px; width: 710px; height: 1px; background: #f0f0f0; }

  .recent h2 { position: absolute; left: 69px; top: 784px; font-size: 11.5px; font-weight: 700; }
  .news-thumb { position: absolute; top: 812px; width: 171px; height: 81px; }
  .thumb-1 { left: 68px;
    background: radial-gradient(ellipse 35% 55% at 60% 25%, rgba(240,140,50,0.85), rgba(240,140,50,0) 100%),
                linear-gradient(180deg, #9a948c 0%, #6e655c 45%, #4a413a 100%); }
  .thumb-2 { left: 258px;
    background: radial-gradient(ellipse 55% 45% at 50% 15%, rgba(255,170,60,0.95), rgba(255,170,60,0) 100%),
                linear-gradient(180deg, #e0862c 0%, #b4461c 40%, #4d3b33 70%, #2f2a28 100%); }
  .thumb-3 { left: 445px;
    background: radial-gradient(ellipse 50% 35% at 45% 50%, rgba(170,110,120,0.5), rgba(170,110,120,0) 100%),
                linear-gradient(180deg, #a6a8ab 0%, #8c8680 40%, #6f665d 75%, #5b5148 100%); }
  .thumb-4 { left: 632px;
    background: radial-gradient(ellipse 40% 50% at 35% 45%, rgba(90,60,40,0.6), rgba(90,60,40,0) 100%),
                linear-gradient(135deg, #8a6446 0%, #b08763 45%, #7c5a3f 75%, #5a4230 100%); }

  .site-footer { position: absolute; left: 0; top: 911px; width: 848px; height: 289px; background: var(--footer); color: var(--footer-text); }
  .footer-col { position: absolute; top: 50px; width: 170px; }
  .footer-col h4 { font-size: 10px; font-weight: 700; color: var(--white); margin-bottom: 19px; }
  .footer-col p, .footer-col li { font-size: 9.5px; font-weight: 300; line-height: 21px; list-style: none; }
  .footer-col strong { font-weight: 700; color: var(--white); }
  .col-contact { left: 69px; }
  .col-pages { left: 251px; }
  .col-posts { left: 433px; width: 180px; }
  .col-posts p { line-height: 19px; margin-bottom: 2px; }
  .col-photos { left: 616px; }
  .col-photos h4 { font-size: 8px; font-weight: 600; color: var(--footer-label); margin-bottom: 10px; }
  .photo-grid { display: grid; grid-template-columns: repeat(4, 30px); grid-auto-rows: 40px; gap: 15px 7px; }
  .photo-grid span { display: block; background: linear-gradient(180deg, #6d7f93, #3f4f60); }
  .photo-grid span:nth-child(2n) { background: linear-gradient(180deg, #9aa39a, #55605c); }
  .photo-grid span:nth-child(3n) { background: linear-gradient(180deg, #cfd6de, #8b98a6); }
  .copyright { position: absolute; left: 69px; top: 264px; font-size: 8px; font-weight: 300; }
  .social { position: absolute; right: 70px; top: 264px; display: flex; gap: 6px; font-size: 7.5px; font-weight: 700; color: var(--white); }
</style>
</head>
<body>
<div class="page">
  <header class="masthead">
    <nav class="site-nav">
      <a class="is-active" href="#">The Tragedy</a>
      <a href="#">Interviews</a>
      <a href="#">Support</a>
      <a href="#">Sponsors</a>
      <a href="#">Media</a>
      <a href="#">Contact</a>
    </nav>
    <div class="hero" role="img" aria-label="Photograph of residents carrying water containers across a dusty hillside above a Nairobi settlement"></div>
    <div class="masthead-rule"></div>
  </header>

  <section class="features">
    <article class="feature">
      <h3>Articles</h3>
      <svg width="26" height="22" viewBox="0 0 26 22"><rect x="1.5" y="1.5" width="23" height="14" rx="1" fill="none" stroke="#333" stroke-width="2"/><rect x="10" y="16" width="6" height="3" fill="#333"/><rect x="7" y="19" width="12" height="2" fill="#333"/></svg>
      <p>Voluptatem accusantium doloremque laudantium sprea totam rem aperiam.</p>
      <div class="btn">Learn more</div>
    </article>
    <article class="feature">
      <h3>Tragedy</h3>
      <svg width="22" height="22" viewBox="0 0 22 22"><path d="M11 21V8" stroke="#333" stroke-width="2"/><path d="M11 9C7 9 4 6 4 2c4 0 7 3 7 7zM11 9c4 0 7-3 7-7-4 0-7 3-7 7zM11 15c-3 0-6-2-7-5 3 0 6 2 7 5zM11 15c3 0 6-2 7-5-3 0-6 2-7 5z" fill="#333"/></svg>
      <p>Voluptatem accusantium doloremque laudantium sprea totam rem aperiam.</p>
      <div class="btn">Learn more</div>
    </article>
    <article class="feature">
      <h3>News</h3>
      <svg width="24" height="22" viewBox="0 0 24 22"><rect x="1.5" y="4.5" width="16" height="16" rx="2" fill="none" stroke="#333" stroke-width="2"/><path d="M9 14l1-4 9-9 3 3-9 9z" fill="#333"/></svg>
      <p>Voluptatem accusantium doloremque laudantium sprea totam rem aperiam.</p>
      <div class="btn">Learn more</div>
    </article>
    <article class="feature">
      <h3>Reasons</h3>
      <svg width="26" height="22" viewBox="0 0 26 22"><path d="M8 5L2 11l6 6M18 5l6 6-6 6M15 3l-4 16" fill="none" stroke="#333" stroke-width="2"/></svg>
      <p>Voluptatem accusantium doloremque laudantium sprea totam rem aperiam.</p>
      <div class="btn">Learn more</div>
    </article>
  </section>
  <div class="section-rule"></div>

  <section class="recent">
    <h2>Recent News</h2>
    <div class="news-thumb thumb-1" role="img" aria-label="News photo of a street fire beside market stalls"></div>
    <div class="news-thumb thumb-2" role="img" aria-label="News photo of crowds in front of burning buildings"></div>
    <div class="news-thumb thumb-3" role="img" aria-label="News photo of people running across open ground"></div>
    <div class="news-thumb thumb-4" role="img" aria-label="News photo of children gathered on earth and debris"></div>
  </section>

  <footer class="site-footer">
    <div class="footer-col col-contact">
      <h4>Get in touch with us</h4>
      <p><strong>Lumina Works Ltd</strong><br>Lumina House suite K12, AB 02<br>Anyplace 20480 Earth</p>
      <p style="margin-top:12px">(555) 010-2200 - (555) 010-2201<br>hello@lumina-demo.com</p>
    </div>
    <div class="footer-col col-pages">
      <h4>Pages</h4>
      <ul><li>Press release</li><li>Terms and conditions</li><li>Privacy policy</li><li>Career center</li><li>Contact us</li></ul>
    </div>
    <div class="footer-col col-posts">
      <h4>Latest posts</h4>
      <p>Lorem ipsum dolor sit amet, consectetur adipiscing elit.</p>
      <p>Pellentesque et pulvinar enim. Quisque at tempor ligula</p>
      <p>Natus error sit voluptatem accusantium doloremque</p>
    </div>
    <div class="footer-col col-photos">
      <h4>Photo stream</h4>
      <div class="photo-grid" role="img" aria-label="Grid of eight small event photographs">
        <span></span><span></span><span></span><span></span><span></span><span></span><span></span><span></span>
      </div>
    </div>
    <p class="copyright">© Lumina 2014 All right reserved. By Templatecraft</p>
    <div class="social"><span>friendnet</span><span>chirper</span><span>linkup</span><span>pinboard</span><span>circles</span></div>
  </footer>
</div>
</body>
</html>
```